Boutique personal training and fitness studio - banner ad design

We need a 'revolving' banner ad designed for our personal training and fitness studio. There are three separate offers (i.e. 3 pages to the advertisements)
Offer 1
PT Starter Pack
3 personal training sessions
$119
New clients only
Offer 2
Group fitness
2 weeks unlimited group fitness classes
$29
New clients only
Offer 3
Strength starter pack
2 weeks unlimited group fitness classes and 2 PT sessions
$89
New clients only
Please do not put the words "Offer 1, 2 or 3" in the ads - just the text following each offer.
Each advertisement should be sized to fit across around half of the webpage and be in landscape format.
Each advertisement should have a suitable picture (no cartoons) and should be complimentary to the existing website.
Each advertisement should also include the logo (attached)
www.corrabankliftworks.com.au
Training

```html
<!DOCTYPE html>
<html lang="en">
<head>
<meta charset="utf-8">
<title>Strength starter pack – Corrabank Liftworks</title>
<link rel="stylesheet" href="https://fonts.googleapis.com/css2?family=Fira+Sans:wght@400;600;700&display=swap">
<style>
  :root {
    --brand-red: #e8232d;
    --brand-black: #0b0b0b;
    --text-white: #ffffff;
    --photo-light: #e9e6e3;
    --photo-mid: #b9b4b0;
    --photo-warm: #d9a9a4;
  }
  * { margin: 0; padding: 0; box-sizing: border-box; }
  html, body {
    width: 1200px;
    height: 376px;
    overflow: hidden;
    background: #ffffff;
  }
  .banner {
    position: relative;
    width: 1200px;
    height: 376px;
    overflow: hidden;
    font-family: "Fira Sans", "Helvetica Neue", Arial, sans-serif;
    background: var(--brand-black);
  }
  .banner__shapes {
    position: absolute;
    inset: 0;
  }
  .offer {
    position: absolute;
    left: 60px;
    top: 50px;
    color: var(--text-white);
  }
  .offer__title {
    font-size: 74px;
    font-weight: 600;
    line-height: 1;
    letter-spacing: -0.5px;
  }
  .offer__details {
    margin-top: 10px;
    font-size: 29px;
    font-weight: 400;
    line-height: 40px;
  }
  .studio-name {
    position: absolute;
    left: 38px;
    top: 292px;
    width: 210px;
    color: var(--text-white);
    font-size: 24px;
    font-weight: 600;
    line-height: 28px;
    text-transform: uppercase;
    letter-spacing: 1px;
  }
  .price {
    position: absolute;
    left: 338px;
    top: 262px;
    color: var(--brand-red);
  }
  .price__amount {
    font-size: 66px;
    font-weight: 400;
    line-height: 1;
  }
  .price__note {
    font-size: 26px;
    font-weight: 400;
    line-height: 1;
    margin-top: 2px;
  }
</style>
</head>
<body>
  <div class="banner">
    <svg class="banner__shapes" width="1200" height="376" viewBox="0 0 1200 376" aria-hidden="false">
      <defs>
        <linearGradient id="photoTone" x1="0" y1="0" x2="1" y2="1">
          <stop offset="0" stop-color="var(--photo-light)"/>
          <stop offset="0.45" stop-color="var(--photo-warm)"/>
          <stop offset="1" stop-color="var(--photo-mid)"/>
        </linearGradient>
      </defs>
      <rect class="band-red" x="0" y="0" width="1200" height="246" fill="var(--brand-red)"/>
      <rect class="band-black" x="0" y="246" width="1200" height="130" fill="var(--brand-black)"/>
      <polygon class="photo-area" points="855,0 1200,0 1200,376 720,376"
               fill="url(#photoTone)" role="img"
               aria-label="Photo of smiling studio members doing crunches on mats in a bright rooftop gym"/>
      <polygon class="flag-block" points="790,0 858,0 848,34 780,34" fill="var(--brand-black)"/>
      <polygon class="flag-block" points="752,44 790,44 780,74 742,74" fill="var(--brand-black)"/>
    </svg>

    <div class="offer">
      <h1 class="offer__title">Strength starter pack</h1>
      <p class="offer__details">2 weeks unlimited group fitness classes<br>and 2 PT sessions</p>
    </div>

    <div class="studio-name">Corrabank Liftworks</div>

    <div class="price">
      <div class="price__amount">$89</div>
      <div class="price__note">New clients only</div>
    </div>
  </div>
</body>
</html>
```